Workers comp/Business Ins/ Payroll- Postcard

I own an insurance agency.  I'm interested in getting some professional advice on how to design a message for what i want to sell.  The products I want to sell are 1) Workers compensation 2) business Insurance 3) Payroll processing. They are integrated together but I'm not sure if it's too much to put on a postcard and if I don't put it on a postcard I could be missing out on sales.
I have the ability to look up what Insurance company a business has their workers compensation  policy with, along with their expiration date.  Based on that information I can tell if the business is overpaying for their Workers compensation. insurance. Most companies are overpaying so I can usually save a company money very quickly if I can get in front of them. Some businesses work with a broker such as myself and buy a policy. When it's done this way, the business ESTIMATES his payroll for the year and at the end of the year they have to complete an audit to find out the actual payroll. Based on audit, they will either owe more money if they were low or get money back if they were high. The other way a business buys a workers comp. policy is with their payroll company. The payroll company will place the policy on Pay -as- you -go which means when you pay your employees every week they  will also calculate how much the workers comp premium is for the week and take that amount out of their checking account. This method avoids large down payments, helps with cash flow and should be very accurate at the end of the policy term.  This is by far the best way to do this for the businessowner. My company also has payroll company and we do this for the insured as well. However, most payroll company's such as QRT and Wagelon charge the customer $15 every time they do this so if it's weekly it is another $780 a year.  We also complete the insured's audit for them which is a big headache for the businessowner.
One of our biggest benefits of doing business with our company is we have a  Steady Rate Forever. When you sign up your base price will never increase. Payroll companies are famous for "discounting a new client" only to increase the rate in a few months later. Our service is also superior to the other payroll companies who use overseas service centers. We have staff within our office and we can answer questions quickly. We usually save businesses money on  their Payroll processing but it's not what we focus on- We focus on the Service.
Business Insurance- One of our main companies that we represent is Brindle Insurance. Brindle is very competitive and we usually write business accounts where we save the business owner money but offer superior coverages.
in summary, I'm offering 1) better workers compensation rates 2) Pay as you go workers comp. 3) Steady Rate, audits done for you, and superior customer service with our payroll company 4) savings on their business insurance with superior coverages.
Sometimes when we talk to an insured we may start with just their payroll and later get the WC and business liability. Each account is different and we do not pressure people to make decisions and we do what is right for them.  The biggest takeaway is we take some things off the plate for the businessowner where they can make just one phone call to get what they need done.  Our Website is www.harbor-mutual.example. my email is tomk@harbor-mutual.example if you have any questions.
Thank You
Tom Kessor

Target Market(s)
Small business owners 1-50 employees
Industry/Entity Type
Insurance and Payroll
Font styles to use
Other font styles liked:
- Let designer choose

Colors
Designer to choose colors to be used in the design.
Requirements
Must have
- It shouldn't be boring- needs to stand out- can use 6x11 inch postcard

Nice to have
- I like humor but not a must

Should not have
- Nothing I can think of

```html
<!DOCTYPE html>
<html lang="en">
<head>
<meta charset="utf-8">
<title>Harbor Mutual – Postcard Design</title>
<link rel="stylesheet" href="https://fonts.googleapis.com/css2?family=Archivo:wght@400;500;600;700;800;900&family=Sora:wght@300;400;600;700;800&display=swap">
<style>
  :root {
    --navy: #343a47;
    --maroon: #7b2d2f;
    --band-gray: #8b8b8b;
    --paper: #eceff2;
    --ink: #1e2026;
    --label-gray: #a3a3a3;
    --white: #ffffff;
  }
  * { box-sizing: border-box; margin: 0; padding: 0; }
  html, body { width: 873px; height: 1200px; overflow: hidden; background: var(--white); }
  body { position: relative; font-family: "Archivo", Arial, sans-serif; color: var(--ink); }

  /* presentation heading */
  .sheet-title { position: absolute; left: 59px; top: 63px; height: 51px; border-left: 2px solid var(--label-gray); padding-left: 13px; font-family: "Sora", sans-serif; color: var(--label-gray); }
  .sheet-title__main { font-size: 30px; font-weight: 400; line-height: 32px; letter-spacing: 0.3px; margin-top: 4px; }
  .sheet-title__sub { font-size: 16px; font-weight: 300; line-height: 17px; }

  .postcard { position: absolute; overflow: hidden; box-shadow: 0 6px 18px rgba(0,0,0,0.12); }
  .postcard__shapes { position: absolute; inset: 0; width: 100%; height: 100%; display: block; }
  .abs { position: absolute; }

  /* FRONT */
  .postcard--front { left: 60px; top: 176px; width: 756px; height: 412px; background: var(--white); }
  .brand-name { font-family: "Archivo", sans-serif; font-weight: 600; color: var(--maroon); letter-spacing: 0.5px; white-space: nowrap; }
  .front-brand { left: 40px; top: 28px; width: 170px; text-align: center; font-size: 21px; line-height: 24px; }
  .headline { left: 25px; top: 107px; color: var(--white); font-weight: 800; font-size: 50px; line-height: 42px; letter-spacing: 0.2px; }
  .service-tag { display: flex; align-items: center; gap: 5px; color: var(--white); font-size: 12px; font-weight: 500; white-space: nowrap; }
  .service-tag svg { width: 12px; height: 12px; flex: none; }
  .tag-1 { left: 23px; top: 216px; }
  .tag-2 { left: 170px; top: 215px; }
  .tag-3 { left: 25px; top: 238px; }

  .benefit-lock { left: 22px; top: 309px; width: 52px; height: 76px; }
  .benefit-kicker { left: 89px; top: 300px; color: var(--white); font-family: "Sora", sans-serif; font-size: 10.5px; font-weight: 300; }
  .benefit-title { left: 88px; top: 312px; color: var(--white); font-family: "Sora", sans-serif; font-weight: 800; font-size: 33px; line-height: 31px; letter-spacing: -0.3px; }
  .benefit-note { left: 89px; top: 376px; color: var(--white); font-size: 10px; white-space: nowrap; }

  .call-box { left: 423px; top: 336px; width: 58px; height: 58px; border-radius: 4px; background: var(--white); display: flex; align-items: center; justify-content: center; }
  .call-box svg { width: 34px; height: 34px; }
  .call-label { left: 499px; top: 340px; color: var(--white); font-family: "Sora", sans-serif; font-weight: 300; font-size: 18px; letter-spacing: 0.8px; white-space: nowrap; }
  .call-number { left: 498px; top: 358px; color: var(--white); font-family: "Sora", sans-serif; font-weight: 600; font-size: 29px; letter-spacing: 2.5px; white-space: nowrap; }

  /* BACK */
  .postcard--back { left: 54px; top: 630px; width: 755px; height: 413px; background: var(--white); }
  .back-brand { left: 258px; top: 16px; width: 112px; text-align: center; font-size: 12px; line-height: 14px; }
  .section-heading { font-weight: 600; font-size: 19px; line-height: 18px; color: var(--ink); }
  .section-heading .accent { color: var(--maroon); display: block; }
  .about-heading { left: 32px; top: 43px; }
  .body-copy { font-size: 8.6px; line-height: 13.4px; color: var(--ink); }
  .about-copy { left: 35px; top: 83px; width: 305px; }
  .services-heading { left: 32px; top: 139px; }
  .services-copy { left: 35px; top: 160px; width: 305px; }
  .service-item { left: 101px; width: 250px; }
  .service-item__title { display: flex; align-items: center; gap: 6px; font-size: 13.5px; font-weight: 500; line-height: 16px; }
  .service-item__title svg { width: 16px; height: 16px; flex: none; }
  .service-item .body-copy { margin-left: 23px; margin-top: 2px; }
  .item-1 { top: 197px; }
  .item-2 { top: 247px; }
  .item-3 { top: 295px; }

  .stamp-box { left: 642px; top: 27px; width: 73px; height: 78px; border: 2px solid var(--navy); }
  .address-line { left: 426px; width: 288px; height: 0; border-top: 1.5px solid var(--navy); }

  .contact-heading { left: 521px; top: 318px; width: 120px; text-align: center; color: var(--white); font-weight: 600; font-size: 20px; }
  .contact-row { display: flex; align-items: flex-start; gap: 6px; color: var(--white); font-size: 8.4px; line-height: 9.5px; }
  .contact-row svg { width: 13px; height: 13px; flex: none; }
  .contact-address { left: 426px; top: 346px; width: 180px; }
  .contact-phone { left: 426px; top: 370px; }
  .contact-email { left: 603px; top: 346px; }
  .contact-web { left: 603px; top: 370px; }
  .contact-row span { padding-top: 2px; }
</style>
</head>
<body>

<header class="sheet-title">
  <div class="sheet-title__main">Post Card Design</div>
  <div class="sheet-title__sub">Design 1</div>
</header>

<!-- Front of postcard -->
<section class="postcard postcard--front" aria-label="Postcard front">
  <svg class="postcard__shapes" viewBox="0 0 1429 779" preserveAspectRatio="none" aria-hidden="false">
    <defs>
      <linearGradient id="officeLight" x1="0" y1="0" x2="1" y2="1">
        <stop offset="0" stop-color="#e9efe9"/>
        <stop offset="0.35" stop-color="#c9d8c2"/>
        <stop offset="0.6" stop-color="#e7e9ea"/>
        <stop offset="1" stop-color="#b9bfc4"/>
      </linearGradient>
    </defs>
    <polygon points="861,0 1429,0 1429,592 490,592" fill="url(#officeLight)" role="img" aria-label="Photo: smiling businessman in a white shirt and tie working on a laptop in a bright office"/>
    <polygon points="0,134 514,134 621,30 648,30 528,164 0,164" fill="var(--band-gray)"/>
    <polygon points="0,164 528,164 606,0 861,0 526,535 0,535" fill="var(--navy)"/>
    <polygon points="614,592 1429,592 1429,779 741,779" fill="var(--navy)"/>
    <polygon points="0,535 576,535 741,779 0,779" fill="var(--maroon)"/>
  </svg>

  <div class="abs brand-name front-brand">Harbor Mutual</div>

  <h1 class="abs headline">INSURANCE<br>AGENCY</h1>

  <div class="abs service-tag tag-1">
    <svg viewBox="0 0 12 12"><circle cx="6" cy="6" r="6" fill="var(--maroon)"/><circle cx="6" cy="6" r="3.4" fill="none" stroke="#fff" stroke-width="0.9"/><path d="M4.4 6.1l1.1 1 2-2.1" fill="none" stroke="#fff" stroke-width="0.9"/></svg>
    Workers compensation
  </div>
  <div class="abs service-tag tag-2">
    <svg viewBox="0 0 12 12"><circle cx="6" cy="6" r="6" fill="var(--maroon)"/><circle cx="6" cy="6" r="3.2" fill="none" stroke="#fff" stroke-width="0.8"/><text x="6" y="7.7" font-size="4.5" text-anchor="middle" fill="#fff" font-family="Arial, sans-serif">$</text></svg>
    Payroll processing
  </div>
  <div class="abs service-tag tag-3">
    <svg viewBox="0 0 12 12"><circle cx="6" cy="6" r="6" fill="var(--maroon)"/><path d="M3.6 5.3L6 3.4l2.4 1.9v3.3H3.6z" fill="none" stroke="#fff" stroke-width="0.9"/><rect x="5.3" y="6.1" width="1.4" height="2.5" fill="#fff"/></svg>
    Business Insurance
  </div>

  <svg class="abs benefit-lock" viewBox="0 0 52 76" aria-hidden="true">
    <path d="M11 34V20a15 15 0 0 1 30 0v14" fill="none" stroke="#fff" stroke-width="6"/>
    <circle cx="26" cy="49" r="25" fill="#fff"/>
    <circle cx="26" cy="49" r="17" fill="var(--maroon)"/>
    <text x="26" y="58" font-size="24" font-weight="700" text-anchor="middle" fill="#fff" font-family="Archivo, sans-serif">$</text>
    <rect x="23" y="68" width="6" height="8" rx="2" fill="#fff"/>
  </svg>
  <div class="abs benefit-kicker">One of our biggest benefits</div>
  <h2 class="abs benefit-title">Steady Rate<br>Forever</h2>
  <p class="abs benefit-note">When you sign up your base price will never increase</p>

  <div class="abs call-box">
    <svg viewBox="0 0 34 34" aria-hidden="true">
      <path d="M7 5c1.5-1 3-1 4 .5l3 4.5c.8 1.2.5 2.5-.6 3.3l-1.8 1.3c1.4 3.2 4 5.8 7.2 7.2l1.3-1.8c.8-1.1 2.1-1.4 3.3-.6l4.5 3c1.5 1 1.5 2.5.5 4l-1.7 2.3c-1 1.3-2.7 1.8-4.2 1.3C14.5 26.8 7.2 19.5 4 11.3c-.5-1.5 0-3.2 1.3-4.2z" fill="none" stroke="var(--navy)" stroke-width="2"/>
      <path d="M20 5a9 9 0 0 1 9 9M20 10a4 4 0 0 1 4 4" fill="none" stroke="var(--navy)" stroke-width="2" stroke-linecap="round"/>
    </svg>
  </div>
  <div class="abs call-label">Call to fine out more</div>
  <div class="abs call-number">+1-555-0142</div>
</section>

<!-- Back of postcard -->
<section class="postcard postcard--back" aria-label="Postcard back">
  <svg class="postcard__shapes" viewBox="0 0 1428 780" preserveAspectRatio="none" aria-hidden="true">
    <rect x="715" y="0" width="713" height="780" fill="var(--paper)"/>
    <polygon points="0,582 438,700 715,780 0,780" fill="var(--navy)"/>
    <polygon points="438,700 1428,522 1428,780 715,780" fill="var(--maroon)"/>
  </svg>

  <div class="abs brand-name back-brand">Harbor Mutual</div>

  <h2 class="abs section-heading about-heading"><span class="accent">About</span>Our Company</h2>
  <p class="abs body-copy about-copy">Lorem ipsum dolor sit amet consectetur adipiscing elit. Quisque faucibus ex sapien vitae pellentesque sem placerat. In id cursus mi pretium tellus duis convallis. Tempus leo eu aenean sed diam urna tempor.</p>

  <h2 class="abs section-heading services-heading">Our Services</h2>
  <p class="abs body-copy services-copy">Lorem ipsum dolor sit amet consectetur adipiscing elit. Quisque faucibus ex sapien vitae pellentesque sem placerat.m urna tempor.</p>

  <div class="abs service-item item-1">
    <div class="service-item__title">
      <svg viewBox="0 0 16 16"><circle cx="8" cy="8" r="8" fill="var(--maroon)"/><circle cx="8" cy="8" r="4.6" fill="none" stroke="#fff" stroke-width="1.1"/><path d="M6 8.2l1.5 1.3 2.6-2.7" fill="none" stroke="#fff" stroke-width="1.1"/></svg>
      Workers compensation
    </div>
    <p class="body-copy">Lorem ipsum dolor sit amet consectetur adipiscing elit.<br>Quisque faucibus ex sapien vitae.</p>
  </div>
  <div class="abs service-item item-2">
    <div class="service-item__title">
      <svg viewBox="0 0 16 16"><circle cx="8" cy="8" r="8" fill="var(--maroon)"/><path d="M4.8 7.2L8 4.6l3.2 2.6v4.3H4.8z" fill="none" stroke="#fff" stroke-width="1.1"/><rect x="7.1" y="8.2" width="1.8" height="3.2" fill="#fff"/></svg>
      Business Insurance
    </div>
    <p class="body-copy">Lorem ipsum dolor sit amet consectetur adipiscing elit.<br>Quisque faucibus ex sapien vitae.</p>
  </div>
  <div class="abs service-item item-3">
    <div class="service-item__title">
      <svg viewBox="0 0 16 16"><circle cx="8" cy="8" r="8" fill="var(--maroon)"/><circle cx="8" cy="8" r="4.4" fill="none" stroke="#fff" stroke-width="1"/><text x="8" y="10.3" font-size="6" text-anchor="middle" fill="#fff" font-family="Arial, sans-serif">$</text></svg>
      Payroll processing
    </div>
    <p class="body-copy">Lorem ipsum dolor sit amet consectetur adipiscing elit.<br>Quisque faucibus ex sapien vitae.</p>
  </div>

  <div class="abs stamp-box" aria-label="Stamp area"></div>
  <div class="abs address-line" style="top:130px"></div>
  <div class="abs address-line" style="top:161px"></div>
  <div class="abs address-line" style="top:192px"></div>
  <div class="abs address-line" style="top:222px"></div>
  <div class="abs address-line" style="top:253px"></div>

  <h2 class="abs contact-heading">Contact</h2>

  <div class="abs contact-row contact-address">
    <svg viewBox="0 0 13 13"><path d="M6.5 12S2.2 7.6 2.2 5a4.3 4.3 0 0 1 8.6 0c0 2.6-4.3 7-4.3 7z" fill="none" stroke="#fff" stroke-width="1"/><circle cx="6.5" cy="5" r="1.5" fill="none" stroke="#fff" stroke-width="1"/></svg>
    <span>Your Address Goes Here, 999 City, Country.</span>
  </div>
  <div class="abs contact-row contact-phone">
    <svg viewBox="0 0 13 13"><path d="M2.6 1.8c.6-.4 1.1-.4 1.5.2l1.1 1.7c.3.5.2.9-.2 1.2l-.7.5c.5 1.2 1.5 2.2 2.7 2.7l.5-.7c.3-.4.8-.5 1.2-.2l1.7 1.1c.6.4.6.9.2 1.5l-.6.9c-.4.5-1 .7-1.6.5C5.4 10.3 2.7 7.6 1.5 4.4c-.2-.6 0-1.2.5-1.6z" fill="none" stroke="#fff" stroke-width="0.9"/><path d="M7.6 1.8a3.6 3.6 0 0 1 3.6 3.6" fill="none" stroke="#fff" stroke-width="0.9"/></svg>
    <span>+1-555-0142</span>
  </div>
  <div class="abs contact-row contact-email">
    <svg viewBox="0 0 13 13"><rect x="1" y="2.5" width="11" height="8" rx="0.8" fill="none" stroke="#fff" stroke-width="1"/><path d="M1.3 3l5.2 4 5.2-4" fill="none" stroke="#fff" stroke-width="1"/></svg>
    <span>tomk@harbor-mutual.example</span>
  </div>
  <div class="abs contact-row contact-web">
    <svg viewBox="0 0 13 13"><circle cx="6.5" cy="6.5" r="5.3" fill="none" stroke="#fff" stroke-width="1"/><ellipse cx="6.5" cy="6.5" rx="2.3" ry="5.3" fill="none" stroke="#fff" stroke-width="0.9"/><path d="M1.2 6.5h10.6" stroke="#fff" stroke-width="0.9"/></svg>
    <span>www.harbor-mutual.example</span>
  </div>
</section>

</body>
</html>
```